Bref créative
meadowlark mobile ultrasound business cards
Meadowlark Mobile Ultrasound
Bright & Fun-filled
Doreen Pavlick, RDMS, RVT
President/Owner
Bayview Springs, FL 33000
info@meadowlarkmobileultrasound.example
www.meadowlarkmobileultrasound.example

```html
<!DOCTYPE html>
<html lang="en">
<head>
<meta charset="utf-8">
<title>Meadowlark Mobile Ultrasound – Business Card</title>
<link rel="stylesheet" href="https://fonts.googleapis.com/css2?family=Marcellus+SC&display=swap">
<style>
  :root {
    --page-bg: #ece8e3;
    --orange-deep: #f26a1b;
    --orange-bright: #ff9a2e;
    --card-white: #ffffff;
    --ink-dark: #3d3d3d;
    --ink-grey: #6e6e6e;
    --accent: #f07a22;
    --rule: #9a9a9a;
  }
  html, body {
    margin: 0;
    width: 1200px;
    height: 914px;
    overflow: hidden;
    background: var(--page-bg);
    font-family: "Marcellus SC", "Times New Roman", serif;
  }
  .canvas {
    width: 1200px;
    height: 914px;
    display: flex;
    align-items: center;
    justify-content: center;
  }
  .business-card {
    position: relative;
    width: 1000px;
    height: 572px;
    box-sizing: border-box;
    padding: 24px;
    background: linear-gradient(135deg, var(--orange-deep), var(--orange-bright) 55%, var(--orange-deep));
    box-shadow: 0 14px 30px rgba(0,0,0,0.18);
  }
  .card-face {
    position: relative;
    width: 100%;
    height: 100%;
    background: var(--card-white);
  }
  .brand {
    position: absolute;
    top: 110px;
    left: 0;
    right: 0;
    display: flex;
    align-items: center;
    justify-content: center;
    gap: 18px;
  }
  .brand-dot {
    width: 58px;
    height: 58px;
    border-radius: 50%;
    background: var(--accent);
    flex: none;
  }
  .brand-name {
    font-size: 38px;
    font-weight: 400;
    color: var(--ink-dark);
    letter-spacing: 1px;
    line-height: 1.05;
    margin: 0;
  }
  .holder {
    position: absolute;
    top: 296px;
    right: 548px;
    text-align: right;
    white-space: nowrap;
  }
  .holder-name {
    font-size: 30px;
    color: var(--accent);
    margin: 0 0 8px;
    letter-spacing: 0.5px;
  }
  .holder-title {
    font-size: 21px;
    color: var(--ink-grey);
    margin: 0;
  }
  .divider {
    position: absolute;
    top: 292px;
    left: 420px;
    width: 1px;
    height: 146px;
    background: var(--rule);
  }
  .contact-list {
    position: absolute;
    top: 294px;
    left: 440px;
    margin: 0;
    padding: 0;
    list-style: none;
    white-space: nowrap;
  }
  .contact-item {
    display: flex;
    align-items: center;
    gap: 10px;
    height: 36px;
    font-size: 19px;
    color: var(--ink-grey);
  }
  .contact-icon {
    width: 22px;
    height: 22px;
    flex: none;
  }
</style>
</head>
<body>
<main class="canvas">
  <section class="business-card" aria-label="Meadowlark Mobile Ultrasound business card">
    <div class="card-face">
      <header class="brand">
        <span class="brand-dot" aria-hidden="true"></span>
        <h1 class="brand-name">Meadowlark<br>Mobile Ultrasound</h1>
      </header>

      <div class="holder">
        <p class="holder-name">Doreen Pavlick, RDMS, RVT</p>
        <p class="holder-title">President/Owner</p>
      </div>

      <div class="divider" aria-hidden="true"></div>

      <ul class="contact-list">
        <li class="contact-item">
          <svg class="contact-icon" viewBox="0 0 22 22" aria-hidden="true">
            <circle cx="11" cy="11" r="11" fill="var(--accent)"/>
            <path d="M11 4.5a4 4 0 0 0-4 4c0 3 4 8 4 8s4-5 4-8a4 4 0 0 0-4-4z" fill="#fff"/>
            <circle cx="11" cy="8.5" r="1.5" fill="var(--accent)"/>
          </svg>
          <span>Bayview Springs, FL 33000</span>
        </li>
        <li class="contact-item">
          <svg class="contact-icon" viewBox="0 0 22 22" aria-hidden="true">
            <circle cx="11" cy="11" r="11" fill="var(--accent)"/>
            <path d="M7.5 5.5l2 .2 1 2.6-1.3 1a7 7 0 0 0 3.5 3.5l1-1.3 2.6 1 .2 2c-.3.8-1.2 1.3-2 1.2A10 10 0 0 1 6.3 7.5c-.1-.8.4-1.7 1.2-2z" fill="#fff"/>
          </svg>
          <span>954-555-0142</span>
        </li>
        <li class="contact-item">
          <svg class="contact-icon" viewBox="0 0 22 22" aria-hidden="true">
            <circle cx="11" cy="11" r="11" fill="var(--accent)"/>
            <rect x="5.5" y="7" width="11" height="8" fill="#fff"/>
            <path d="M5.5 7l5.5 4.5L16.5 7" fill="none" stroke="var(--accent)" stroke-width="1.2"/>
          </svg>
          <span>info@meadowlarkmobileultrasound.example</span>
        </li>
        <li class="contact-item">
          <svg class="contact-icon" viewBox="0 0 22 22" aria-hidden="true">
            <circle cx="11" cy="11" r="11" fill="var(--accent)"/>
            <circle cx="11" cy="11" r="5.5" fill="none" stroke="#fff" stroke-width="1.3"/>
            <ellipse cx="11" cy="11" rx="2.3" ry="5.5" fill="none" stroke="#fff" stroke-width="1.1"/>
            <line x1="5.5" y1="11" x2="16.5" y2="11" stroke="#fff" stroke-width="1.1"/>
          </svg>
          <span>www.meadowlarkmobileultrasound.example</span>
        </li>
      </ul>
    </div>
  </section>
</main>
</body>
</html>
```